Header für Blog zur Organisationsentwicklung
LunaKrie hat die Hinweise im Briefing und in den Kommentaren zu vorhandenen Designs gut aufgenommen und den Gestaltungsprozess vorangetrieben. So bekomme ich ein tolles Design, wo ich vorher keine Ahnung hatte, wie es aussehen sollte.
Zielgruppe
Ich bin freiberuflicher Organisationsberater und pflege auf meiner Website ein Blog zur Organisationsentwicklung. Dieses Blog soll zukünftig auf einer eigenen Domain erscheinen, sodass auch andere Kollegen sich daran beteiligen können. Daher soll mein Name nicht mehr im Vordergrund stehen - wenngleich ich immer noch als der Macher des Blog erkennbar bleiben soll.
Aufgabenstellung
Für das Blog "Labor für Unternehmenswandel" www.uw-labor.de wird ein ansprechender Header gesucht.
Der Header sollte den Namen des Blog und ein grafisches Element enthalten, dass der Bildsprache "Werkstatt", "Organisation", "Führung", etc. entnommen ist. Eventuell ein Element, das die Bildsprachen verbindet?
Da das Blog von einem Foto-Slider unter dem Header geprägt ist, sollte der Header nicht einfach aus einem Foto bestehen.
Die Farbgebung des Blog stellt die grafische Verbindung zu meiner Website www.hasselkamp.com her.
Mein Logo sollte im Header nicht verwendet werden, da ich das Blog bewusst von meiner Website löse, um weitere Beraterkollegen einzuladen, dabei mitzumachen

```html
<!DOCTYPE html>
<html lang="de">
<head>
<meta charset="utf-8">
<title>Labor für Unternehmenswandel – Header</title>
<link rel="stylesheet" href="https://fonts.googleapis.com/css2?family=Fira+Sans:wght@600&display=swap">
<style>
  :root {
    --navy-deep: #2f2d69;
    --navy-soft: #5a5b91;
    --navy-mid: #45457d;
    --white: #ffffff;
    --icon-ink: #2f2d69;
  }
  html, body {
    margin: 0;
    padding: 0;
    overflow: hidden;
    background: var(--white);
  }
  .blog-header {
    position: relative;
    width: 1200px;
    height: 102px;
    overflow: hidden;
    background: var(--navy-deep);
  }
  .blog-header__backdrop {
    position: absolute;
    inset: 0;
  }
  .blog-header__icons {
    position: absolute;
    left: 0;
    top: 0;
  }
  .blog-header__title {
    position: absolute;
    left: 250px;
    right: 0;
    top: 22px;
    margin: 0;
    text-align: center;
    font-family: "Fira Sans", "Helvetica Neue", Arial, sans-serif;
    font-weight: 600;
    font-size: 40px;
    line-height: 52px;
    letter-spacing: 0.2px;
    color: var(--white);
  }
</style>
</head>
<body>
  <header class="blog-header">
    <svg class="blog-header__backdrop" width="1200" height="102" viewBox="0 0 1200 102" aria-hidden="true">
      <!-- broad light sweep -->
      <ellipse cx="640" cy="250" rx="760" ry="290" fill="var(--navy-soft)"/>
      <!-- dark lower arc -->
      <ellipse cx="700" cy="330" rx="640" ry="255" fill="var(--navy-deep)"/>
      <!-- soft inner band along the lower arc -->
      <ellipse cx="700" cy="330" rx="600" ry="238" fill="var(--navy-mid)" opacity="0.35"/>
      <ellipse cx="700" cy="340" rx="570" ry="240" fill="var(--navy-deep)"/>
      <!-- dark top-right corner -->
      <ellipse cx="1180" cy="-150" rx="330" ry="190" fill="var(--navy-deep)"/>
      <!-- dark top-left corner -->
      <ellipse cx="-60" cy="-60" rx="160" ry="90" fill="var(--navy-deep)"/>
    </svg>

    <svg class="blog-header__icons" width="240" height="102" viewBox="0 0 240 102" aria-hidden="true">
      <!-- wrench tile -->
      <g class="icon-tile icon-tile--wrench" transform="translate(46 30)">
        <rect width="34" height="38" rx="6" fill="var(--white)"/>
        <g transform="rotate(-45 17 19)" fill="var(--icon-ink)">
          <rect x="14.5" y="13" width="5" height="20" rx="2.5"/>
          <path d="M10 6 a7 7 0 0 0 14 0 v7 a7 7 0 0 1 -14 0 z"/>
          <circle cx="17" cy="10" r="7"/>
          <rect x="14.5" y="2" width="5" height="8" fill="var(--white)"/>
        </g>
      </g>
      <!-- organisation chart tile -->
      <g class="icon-tile icon-tile--org" transform="translate(112 14)">
        <rect width="34" height="38" rx="6" fill="var(--white)"/>
        <g fill="var(--icon-ink)">
          <rect x="12" y="7" width="10" height="8" rx="1"/>
          <rect x="16" y="15" width="2" height="5"/>
          <rect x="7" y="19" width="20" height="2"/>
          <rect x="7" y="19" width="2" height="5"/>
          <rect x="16" y="19" width="2" height="5"/>
          <rect x="25" y="19" width="2" height="5"/>
          <rect x="3.5" y="24" width="9" height="7" rx="1"/>
          <rect x="12.5" y="24" width="9" height="7" rx="1"/>
          <rect x="21.5" y="24" width="9" height="7" rx="1"/>
        </g>
      </g>
      <!-- person tile -->
      <g class="icon-tile icon-tile--person" transform="translate(177 30)">
        <rect width="34" height="38" rx="6" fill="var(--white)"/>
        <g fill="var(--icon-ink)">
          <circle cx="17" cy="13" r="7"/>
          <path d="M5 34 v-4 a9 9 0 0 1 9 -9 h6 a9 9 0 0 1 9 9 v4 z"/>
        </g>
      </g>
    </svg>

    <h1 class="blog-header__title">Labor für Unternehmenswandel</h1>
  </header>
</body>
</html>
```